Marlow Crest Group (Real Estate and Investment)

A high end, clean design.
We are a real estate company with sales, asset management and investment divisions. We want to use a black and white scheme which is really high end feel. The back of the card can just be the logo (black background with the white writing) as we will probably emboss this when we print)

Target Market(s)

High level investors, high end houses for sale

Industry/Entity Type

Business

Contact Information for Business Card

Name, position, phone number and email address
Glen Varley, Managing Director, 0437259064 and glen@marlowcrest-example.com.au

Requirements
Must have
• Back of the card to be the black background with the white writing (as per the attached images). Would like the capacity to emboss the writing and logo

```html
<!DOCTYPE html>
<html lang="en">
<head>
<meta charset="utf-8">
<title>Marlow Crest Group — Business Card</title>
<link href="https://fonts.googleapis.com/css2?family=Poppins:wght@300;400;500&display=swap" rel="stylesheet">
<style>
  :root {
    --stage: #2b2b2d;
    --card-black: #121212;
    --card-white: #ffffff;
    --ink-white: #f4f4f4;
    --ink-name: #4a4a4a;
    --ink-body: #3c3c3c;
    --rule: #8a8a8a;
  }
  * { margin: 0; padding: 0; box-sizing: border-box; }
  html, body {
    width: 1200px;
    height: 1000px;
    overflow: hidden;
    background: var(--stage);
    font-family: "Poppins", sans-serif;
  }
  .card {
    position: absolute;
    left: 250px;
    width: 700px;
    height: 420px;
    box-shadow: 0 10px 30px rgba(0,0,0,0.45);
  }
  .card-back {
    top: 55px;
    background: var(--card-black);
  }
  .card-front {
    top: 525px;
    background: var(--card-white);
  }
  .brand {
    position: absolute;
    left: 60px;
    bottom: 60px;
    display: flex;
    align-items: center;
    gap: 16px;
  }
  .brand-dot {
    width: 26px;
    height: 26px;
    border-radius: 50%;
    border: 1.5px solid var(--ink-white);
  }
  .brand-name {
    color: var(--ink-white);
    font-weight: 400;
    font-size: 25px;
    letter-spacing: 0.5px;
  }
  .contact {
    position: absolute;
    left: 60px;
    top: 60px;
  }
  .contact-name {
    color: var(--ink-name);
    font-weight: 500;
    font-size: 27px;
    line-height: 1.1;
  }
  .contact-role {
    color: var(--ink-name);
    font-weight: 400;
    font-size: 15px;
    margin-top: 4px;
  }
  .contact-rule {
    width: 44px;
    height: 1px;
    background: var(--rule);
    margin: 14px 0 12px;
  }
  .contact-line {
    color: var(--ink-body);
    font-weight: 300;
    font-size: 16px;
    line-height: 1.55;
  }
</style>
</head>
<body>
  <section class="card card-back">
    <div class="brand">
      <span class="brand-dot"></span>
      <span class="brand-name">MARLOW CREST GROUP</span>
    </div>
  </section>

  <section class="card card-front">
    <div class="contact">
      <h1 class="contact-name">Glen Varley</h1>
      <p class="contact-role">Managing Director</p>
      <div class="contact-rule"></div>
      <p class="contact-line">P: 0437259064</p>
      <p class="contact-line">E: glen@marlowcrest-example.com.au</p>
    </div>
  </section>
</body>
</html>
```